Electrical panel service sticker w Bucket truck & Logo

We have a rather plain sticker we put on lighting panels to remind customers who to call for service. We want to redesign them with brushed aluminum background. We want a remake of the sticker with the outline of a bucket truck. You'll need to find or draw the outling of a bucket truck maybe with the boom up slightly as we will get these stickers die cut.

We want LOGO with Ph.# and Email.
Electrical * Lighting * Sign Service

Target Market(s)

Commercial property managers

Industry/Entity Type

Property Management

Requirements
Must have
• Bucket Truck Outline

```html
<!DOCTYPE html>
<html lang="en">
<head>
<meta charset="UTF-8">
<title>Lampline Maintenance – Panel Service Sticker</title>
<link href="https://fonts.googleapis.com/css2?family=Montserrat:wght@700;800;900&display=swap" rel="stylesheet">
<style>
  :root {
    --ink: #0b0b0b;
    --alu-dark: #8a8b88;
    --alu-mid: #b9bab6;
    --alu-light: #eef0ec;
    --art-tone: #151515;
  }
  * { margin: 0; padding: 0; box-sizing: border-box; }
  html, body { width: 1200px; height: 1200px; overflow: hidden; }
  body { font-family: "Montserrat", Arial, sans-serif; }

  .sticker {
    position: relative;
    width: 1200px;
    height: 1200px;
    overflow: hidden;
    background:
      repeating-linear-gradient(180deg, rgba(255,255,255,0.10) 0 1px, rgba(0,0,0,0.05) 1px 2px, rgba(255,255,255,0) 2px 4px),
      repeating-linear-gradient(180deg, rgba(0,0,0,0.04) 0 3px, rgba(255,255,255,0.06) 3px 7px, rgba(0,0,0,0) 7px 11px),
      linear-gradient(90deg, var(--alu-dark) 0%, var(--alu-mid) 22%, var(--alu-light) 52%, #d6d8d3 62%, var(--alu-mid) 82%, var(--alu-dark) 100%);
  }

  .truck-art {
    position: absolute;
    left: 283px;
    top: 93px;
    width: 633px;
    height: 469px;
    background: radial-gradient(ellipse at 50% 60%, #2a2a2a 0%, var(--art-tone) 70%);
    border-radius: 6px;
  }

  .wordmark, .contact {
    position: absolute;
    left: 0;
    top: 0;
  }
  .wordmark text, .contact text {
    fill: var(--ink);
    font-family: "Montserrat", Arial, sans-serif;
  }
  .brand-name { font-weight: 800; font-size: 134px; }
  .tagline { font-weight: 800; font-size: 52px; }
  .service-label { font-weight: 800; font-size: 56px; }
  .service-phone { font-weight: 800; font-size: 80px; }
  .service-email { font-weight: 800; font-size: 46px; }
  .rule { stroke: var(--ink); stroke-width: 3; }
  .icon { fill: var(--ink); }
  .icon-stroke { fill: none; stroke: var(--ink); stroke-width: 3; stroke-linecap: round; }
</style>
</head>
<body>
<main class="sticker">
  <div class="truck-art" role="img" aria-label="Silhouette of a bucket truck with its boom raised and the bucket lifted at the top"></div>

  <svg class="wordmark" width="1200" height="1200" viewBox="0 0 1200 1200">
    <text class="brand-name" x="599" y="674" text-anchor="middle">LAMPLINE</text>
    <text class="brand-name" x="599" y="801" text-anchor="middle" textLength="1059" lengthAdjust="spacing">MAINTENANCE</text>
    <line class="rule" x1="70" y1="822" x2="1129" y2="822"/>
    <text class="tagline" x="70" y="882" textLength="1059" lengthAdjust="spacing">ELECTRICAL | LIGHTING | SIGN SERVICE</text>
    <line class="rule" x1="70" y1="910" x2="1129" y2="910"/>
  </svg>

  <svg class="contact" width="1200" height="1200" viewBox="0 0 1200 1200">
    <text class="service-label" x="75" y="1031" textLength="399" lengthAdjust="spacing">FOR SERVICE</text>
    <g class="phone-icon" transform="translate(496 990)">
      <path class="icon" d="M6 2 L14 0 L20 12 L14 17 Q18 27 27 32 L32 26 L43 32 L41 40 Q36 44 28 42 Q10 35 2 16 Q0 8 6 2 Z"/>
      <path class="icon-stroke" d="M27 14 Q32 15 33 20"/>
      <path class="icon-stroke" d="M28 7 Q38 9 40 19"/>
      <path class="icon-stroke" d="M29 0 Q44 2 46 18"/>
    </g>
    <text class="service-phone" x="562" y="1031" textLength="556" lengthAdjust="spacingAndGlyphs">800-555-0199</text>

    <path class="icon" d="M76 1084 L127 1063 L116 1110 L101 1097 L93 1106 L92 1093 L119 1070 L88 1090 Z"/>
    <text class="service-email" x="148" y="1098" textLength="976" lengthAdjust="spacingAndGlyphs">SERVICE@LAMPLINEMAINTENANCE.COM</text>
  </svg>
</main>
</body>
</html>
```